ZEPRILO.COM is a premium domain sales company. Our competitors are companies like vastplots.example, getparcels.example, peerwords.example. Our current site is at www.zeprilos.example.

We want to have the ability to search for domains, to highlight special offers and have some testimonials on the index page.

The logo for the site is attached.

Please be sure that the order form fits on the screen without scrolling the page. I want the entire form, including the submit button to fit without any page scrolling.

Delivered product - INDEX PAGE, ORDER FORM AND CONTENT PAGE PSDs.

Target Market(s)

Small to Medium business professionals

Industry/Entity Type

It Company

Requirements
Must have
• 1. List of domains for sale
2. Simple search box with button to run the search
3. link for advanced search
4. testimonial area. Note - this can be a small box where a different testimonial is displayed on each page load.
Nice to have
• Would like the site to have some white space. Don't want a heavily packed website. Give it an "airy" feel.

```html
<!DOCTYPE html>
<html lang="en">
<head>
<meta charset="utf-8">
<title>ZEPRILO.COM – Premium Domains</title>
<link href="https://fonts.googleapis.com/css2?family=PT+Sans:wght@400;700&display=swap" rel="stylesheet">
<style>
  :root {
    --green: #0bb04b;
    --green-dark: #0a7a3e;
    --blue: #0b4a94;
    --blue-deep: #08336e;
    --panel-bg: #e8e6e2;
    --panel-frame: #8f8f8f;
    --link-blue: #1a1ae6;
    --accent-yellow: #e8dc8a;
    --quote-red: #ff3b2f;
    --chip: #e6e6e6;
    --ink: #111;
    --white: #fff;
  }
  * { box-sizing: border-box; margin: 0; padding: 0; }
  html, body { width: 1200px; height: 1000px; overflow: hidden; background: var(--white); }
  body { position: relative; font-family: "PT Sans", sans-serif; color: var(--ink); }
  .abs { position: absolute; }

  .brand { left: 375px; top: 36px; font-size: 30px; font-weight: 700; color: var(--blue); letter-spacing: -0.5px; }

  .main-nav { left: 353px; top: 82px; width: 516px; height: 26px; background: var(--green);
    display: flex; align-items: center; justify-content: space-around; padding: 0 10px; }
  .main-nav a { color: var(--white); text-decoration: none; font-size: 14px; }

  .hero { left: 353px; top: 110px; width: 516px; height: 258px; background: var(--blue); }
  .hero-visual { left: 12px; top: 15px; width: 218px; height: 228px;
    background: linear-gradient(180deg, #3fa6ea 0%, #1565b8 45%, #0a2240 100%); }
  .hero-copy { left: 240px; top: 0; width: 270px; height: 258px; color: var(--white); font-size: 13.5px; text-align: center; }
  .hero-copy p { position: absolute; left: 0; width: 100%; }

  .search-label { left: 372px; top: 407px; font-size: 14px; }
  .results-panel { left: 353px; top: 476px; width: 306px; height: 364px; background: var(--panel-bg);
    border: 11px solid var(--panel-frame); border-radius: 18px; }
  .search-bar { left: 365px; top: 432px; width: 285px; height: 59px; border-radius: 6px;
    background: linear-gradient(180deg, #0d57a8 0%, var(--blue-deep) 100%); }
  .search-input { left: 28px; top: 14px; color: var(--white); font-size: 14px; }
  .search-underline { left: 2px; top: 29px; width: 199px; height: 2px; background: var(--accent-yellow); }
  .search-button { left: 214px; top: 8px; width: 50px; height: 44px; background: var(--green); border-radius: 4px;
    box-shadow: 0 0 4px rgba(0,0,0,.5); border: none; }
  .advanced-search { left: 365px; top: 478px; width: 141px; height: 44px; background: var(--green); border-radius: 4px;
    color: var(--white); font-size: 14px; padding: 13px 7px; box-shadow: 1px 2px 3px rgba(0,0,0,.3); }

  .domain-table-head { top: 539px; font-size: 17px; color: var(--link-blue); }
  .domain-table-rule { left: 375px; top: 559px; width: 251px; height: 2px; background: var(--blue-deep); }
  .domain-row { font-size: 14px; }
  .buy-link { color: var(--green); }

  .testimonial-tab { left: 664px; top: 430px; width: 35px; height: 128px; background: var(--green-dark); border-radius: 4px 0 0 4px;
    color: var(--white); font-size: 10px; line-height: 9.6px; text-align: center; padding-top: 7px; font-weight: 700; }
  .testimonial { left: 695px; width: 173px; background: var(--green); border: 2px solid var(--green-dark); border-radius: 4px;
    box-shadow: 1px 2px 3px rgba(0,0,0,.3); }
  .testimonial-quote { font-size: 7.5px; line-height: 15px; }
  .testimonial-author { right: 3px; background: var(--chip); border-radius: 4px; font-size: 9px; padding: 4px 8px; }

  .promo-visual { left: 673px; top: 695px; width: 195px; height: 218px;
    background: linear-gradient(180deg, #f0c4a4 0%, #e23c3c 45%, #d82a2a 75%, #1d1d1d 100%); border-radius: 40% 40% 6px 6px; }

  .site-footer { left: 353px; top: 915px; width: 516px; height: 58px; background: var(--blue); }
  .social-square { top: 16px; width: 30px; height: 28px; background: var(--chip); border-radius: 4px; }
  .copyright { right: 21px; top: 22px; color: var(--white); font-size: 10px; }
</style>
</head>
<body>
  <div class="abs brand">ZEPRILO</div>

  <nav class="abs main-nav">
    <a href="#">Home</a><a href="#">Contact Us</a><a href="#">FAQs</a><a href="#">Domains Sale</a><a href="#">Testimonials</a><a href="#">Cart</a>
  </nav>

  <section class="abs hero">
    <div class="abs hero-visual" role="img" aria-label="Business team around a table against a glowing world map and city skyline"></div>
    <div class="abs hero-copy">
      <p style="top:33px">Let’s your Door is wide open to the world</p>
      <p style="top:79px">by Buying this PREMIUM DOMAIN !</p>
      <p style="top:134px">Impression of Your business could be</p>
      <p style="top:192px">started from Name of the Domain its self.</p>
    </div>
  </section>

  <div class="abs search-label">Search for a Domain</div>
  <div class="abs results-panel"></div>
  <form class="abs search-bar">
    <span class="abs search-input">Enter name of Domain</span>
    <span class="abs search-underline"></span>
    <button class="abs search-button" type="submit" aria-label="Search"></button>
  </form>
  <a class="abs advanced-search">Advance search</a>

  <span class="abs domain-table-head" style="left:376px">DOMAIN</span>
  <span class="abs domain-table-head" style="left:498px">PRIZE</span>
  <span class="abs domain-table-head" style="left:581px">BUY</span>
  <div class="abs domain-table-rule"></div>

  <span class="abs domain-row" style="left:365px;top:584px">DomainName1.com</span><span class="abs domain-row" style="left:498px;top:584px">$1,005</span><span class="abs domain-row buy-link" style="left:571px;top:584px">Buy now</span>
  <span class="abs domain-row" style="left:365px;top:640px">DomainName2.com</span><span class="abs domain-row" style="left:498px;top:640px">$2,015</span><span class="abs domain-row buy-link" style="left:571px;top:640px">Buy now</span>
  <span class="abs domain-row" style="left:365px;top:695px">DomainName3.com</span><span class="abs domain-row" style="left:498px;top:695px">$3,025</span><span class="abs domain-row buy-link" style="left:571px;top:695px">Buy now</span>
  <span class="abs domain-row" style="left:365px;top:749px">DomainName4.com</span><span class="abs domain-row" style="left:498px;top:749px">$4,035</span><span class="abs domain-row buy-link" style="left:571px;top:749px">Buy now</span>
  <span class="abs domain-row" style="left:365px;top:799px">DomainName5.com</span><span class="abs domain-row" style="left:498px;top:799px">$5,045</span><span class="abs domain-row buy-link" style="left:571px;top:799px">Buy now</span>

  <div class="abs testimonial-tab">T<br>E<br>S<br>T<br>I<br>M<br>O<br>N<br>I<br>A<br>L<br>S</div>
  <div class="abs testimonial" style="top:408px;height:91px">
    <p class="abs testimonial-quote" style="left:14px;top:6px;color:var(--quote-red)">We would like to thank to ZEPRILO.COM<br>for a gorgeous name Domain that<br>We were looking for.</p>
    <span class="abs testimonial-author" style="top:59px">Mr Joy Man</span>
  </div>
  <div class="abs testimonial" style="top:503px;height:90px">
    <p class="abs testimonial-quote" style="left:0;width:100%;top:10px;text-align:center;color:var(--white)">Thank to ZEPRILO.COM ,<br>We are satisfy &nbsp;with the Domain name<br>we bought from you.</p>
    <span class="abs testimonial-author" style="top:65px;font-size:10px">Expert Corp</span>
  </div>

  <div class="abs promo-visual" role="img" aria-label="Happy young woman in a red top cheering with raised fists"></div>

  <footer class="abs site-footer">
    <span class="abs social-square" style="left:27px" role="img" aria-label="Social profile link"></span>
    <span class="abs social-square" style="left:70px" role="img" aria-label="Social profile link"></span>
    <span class="abs copyright">Copyrights 2013</span>
  </footer>
</body>
</html>
```